Generator Control - Superyacht Power Management System

We need a graphic design for a Touch Screen interface to control generators on Superyachts. We have a layout of the control system worked out, but need nice graphics to go with it.
The graphics comes down to a 300x460px App that i replicate several times on my 15" touchscreen as required.
See attached images.
The interface is divided up into 4 sections:
• Section#1 - 4 rectangles for the control
• Section#2 - a vertical bar graph,
• Section#3 - a section to display custom information
• Section#4 - a circuit breaker symbol.
The dimensions in pixels must be as per the attached image.
SECTION#1:
The 4 control rectangles correspond to 4 control modes:
• STOP – colours based on RED
• RUN – colours based on ORANGE
• RUN ONLINE – colours based on GREEN
• AUTO – colours based on BLUE
• THE TEXT DOESN’T HAVE TO BE ON THE GRAPHICS, WE JUST NEED THE BACKGROUND FOR THE TEXT, I ADD THE TEXT LATER USING SOFTWARE.
Each control rectangle needs to have 3 clearly identifiable states:
• Active/Selected (this is the currently active mode)
• Not Active/Not Selected (this mode is available but not currently active)
• Unavailable (this mode is not available)
SECTION#2:
The vertical bar graph design only needs the outline/frame of the bar graph. The actual moving part can be left blank; I will add that in later using an animation.
SECTION#3:
Free to look good as you want. See attached image for reference.
Within section#3 (at the top) is a 40x240px subsection, and should simply by 2 states, green or 'background colour of section#3 '. (green for when the generator is running, blend with the rest of section#3 when it is not). There are about 10 different texts I add on top of that square using software, corresponding to the status of the generator (starting, deloading, synchronizing, etc.)
SECTION#4:
Graphical representation of an electrical switch. Can be in two positions: opened or closed. See attached image as reference.

Cheif Engineers /Captains on Superyachts

Graphic Design

• Must have the same graphics style as the uploaded file#2

```html
<!DOCTYPE html>
<html lang="en">
<head>
<meta charset="utf-8">
<title>Generator Control</title>
<link href="https://fonts.googleapis.com/css2?family=Arimo:wght@400;700&display=swap" rel="stylesheet">
<style>
:root{
  --bg:#000;
  --frame:#2b3366;
  --frame-hi:#3c4680;
  --panel:#050509;
  --field:#0b0c1c;
  --field-border:#3a4170;
  --text:#d6d8e0;
  --label:#c4c6d0;
  --dim:#5c5f70;
  --green:#6fa349;
  --green-dark:#3b6a26;
  --orange:#c47c1c;
  --blue:#1f78a8;
}
*{margin:0;padding:0;box-sizing:border-box}
html,body{width:1200px;height:901px;overflow:hidden;background:var(--bg)}
body{font-family:"Arimo",Arial,sans-serif;color:var(--text);position:relative}

.generator{position:absolute;top:224px;width:456px;height:576px;border:1px solid var(--frame);border-radius:9px;background:var(--panel)}
.generator--port{left:116px}
.generator--starboard{left:633px}

.gen-header{position:absolute;left:0;top:0;width:100%;height:28px;border-bottom:1px solid var(--frame);border-radius:8px 8px 0 0;background:linear-gradient(#1a1c2e,#07080f);font-size:15px;line-height:28px}
.gen-title{position:absolute;left:14px}
.gen-readout{position:absolute;right:14px;display:flex;gap:10px}
.gen-readout .sep{width:1px;height:18px;margin-top:5px;background:#555a78}
.gen-readout small{font-size:11px}

.breaker{position:absolute;left:183px;top:-124px;width:92px;height:152px;border:1px solid var(--frame-hi);border-radius:12px 12px 0 0;background:#000}
.breaker svg{position:absolute;left:0;top:0}

.controls{position:absolute;left:0;top:28px;width:366px;height:246px;display:grid;grid-template-columns:183px 183px;grid-template-rows:123px 123px}
.mode{display:flex;align-items:center;justify-content:center;text-align:center;font-size:24px;line-height:1.25;border:1px solid #1b1d28}
.mode--online.is-off{background:linear-gradient(#1d2a16,#0d170a);color:#3f5a30}
.mode--run.is-active{background:linear-gradient(#c8892c 0%,#b06d18 48%,#a0600f 52%,#b87a20 100%);color:#f4ead8}
.mode--stop.is-off{background:linear-gradient(#2a0505,#140000);color:#6e2222}
.mode--auto.is-active{background:linear-gradient(#6aa6c4 0%,#3c87ad 48%,#0f6595 52%,#1b6fa0 100%);color:#eef4f8}
.mode--online.is-active{background:linear-gradient(#8dbf68 0%,#6fa349 48%,#4f8b2c 52%,#5c963a 100%);color:#f2f6ee}
.mode.is-ready{background:linear-gradient(#2a2a2c 0%,#1e1e20 48%,#141416 52%,#1c1c1e 100%);color:#a6a8ae}
.mode--auto.is-off{background:linear-gradient(#0f1b26,#06101a);color:#566878}

.status{position:absolute;left:0;top:274px;width:366px;height:32px;border-top:1px solid #223;border-bottom:1px solid #223;text-align:center;font-size:16px;line-height:32px;letter-spacing:.5px}
.status.is-running{background:linear-gradient(#83b55c,#5d933a 50%,#3f7424 52%,#4c8230);color:#e6ecdc}

.info{position:absolute;left:0;top:306px;width:366px;height:270px}
.info-divider{position:absolute;left:181px;top:0;height:100%;border-left:1px dotted #3a3e55}
.label{position:absolute;font-size:16px;line-height:18px;color:var(--label)}
.label--center{left:15px;width:151px;text-align:center}
.label--side{left:212px;width:40px;text-align:right;font-size:15px}
.field{position:absolute;height:29px;border:1px solid var(--field-border);border-radius:5px;background:linear-gradient(#12142a,#05060e);font-size:16px;line-height:27px;text-align:center;color:var(--text)}
.field--wide{left:15px;width:151px}
.field--short{left:258px;width:76px}
.field--mid{left:219px;width:115px}
.field--time{display:flex;justify-content:space-around;padding:0 4px}

.load{position:absolute;left:368px;top:28px;width:87px;height:547px;border-left:1px solid var(--frame)}
.scale-mark{position:absolute;left:0;width:46px;height:0}
.scale-mark span{position:absolute;right:30px;top:-8px;font-size:11px;color:#ddd}
.scale-mark::before{content:"";position:absolute;left:24px;right:0;top:-1px;border-top:1px solid #ccc}
.tube{position:absolute;left:47px;top:19px;width:31px;height:522px;border:1px solid #555;border-radius:8px;background:#111;display:flex;flex-direction:column;padding:2px 3px;gap:2px}
.seg{flex:1;border-radius:5px;background:linear-gradient(90deg,#1a1a1a,#4a4a4a 45%,#262626);border:1px solid #333}
.seg.is-lit{background:linear-gradient(90deg,#2e4a1e,#7bb055 45%,#3d6328);border-color:#4a7232}
</style>
</head>
<body>

<section class="generator generator--port">
  <div class="breaker" aria-label="Breaker open">
    <svg width="92" height="152" viewBox="0 0 92 152">
      <defs><linearGradient id="pole" x1="0" x2="1"><stop offset="0" stop-color="#666"/><stop offset=".5" stop-color="#eee"/><stop offset="1" stop-color="#777"/></linearGradient></defs>
      <rect x="42" y="21" width="7" height="30" fill="url(#pole)"/>
      <line x1="19" y1="55" x2="44" y2="115" stroke="url(#pole)" stroke-width="7"/>
      <path d="M20 152 v-14 a10 10 0 0 1 10 -10 h32 a10 10 0 0 1 10 10 v14" fill="#000" stroke="#3c4680"/>
    </svg>
  </div>
  <header class="gen-header"><span class="gen-title">Port Generator</span><span class="gen-readout">0%</span></header>
  <div class="controls">
    <div class="mode mode--online is-off">RUN ONLINE</div>
    <div class="mode mode--run is-active">RUN</div>
    <div class="mode mode--stop is-off">STOP</div>
    <div class="mode mode--auto is-active">AUTOMATIC<br>1</div>
  </div>
  <div class="status is-running">RUNNING : OFFLINE</div>
  <div class="info">
    <div class="info-divider"></div>
    <div class="label label--center" style="top:11px">WATER TEMP</div>
    <div class="field field--wide" style="top:34px">83°C</div>
    <div class="label label--center" style="top:76px">OIL PRESSURE</div>
    <div class="field field--wide" style="top:98px">3.8 BAR</div>
    <div class="label label--center" style="top:140px">RPM</div>
    <div class="field field--wide" style="top:162px">1500</div>
    <div class="label label--center" style="top:204px">ONLINE TIME</div>
    <div class="field field--wide field--time" style="top:226px"><span>0h</span><span>0m</span><span>0s</span></div>

    <div class="label label--side" style="top:16px">VAC</div>
    <div class="field field--short" style="top:10px">230</div>
    <div class="label label--side" style="top:46px">VAC</div>
    <div class="field field--short" style="top:40px">400</div>
    <div class="field field--mid" style="top:69px">50.0HZ</div>
    <div class="label label--side" style="top:112px">A L1</div>
    <div class="field field--short" style="top:106px">0</div>
    <div class="label label--side" style="top:142px">A L2</div>
    <div class="field field--short" style="top:136px">0</div>
    <div class="label label--side" style="top:171px">A L3</div>
    <div class="field field--short" style="top:165px">0</div>
    <div class="label label--side" style="top:211px">KVA</div>
    <div class="field field--short" style="top:205px">0</div>
    <div class="label label--side" style="top:238px">PF</div>
    <div class="field field--short" style="top:232px">0.00</div>
  </div>
  <div class="load">
    <div class="scale-mark" style="top:16px"><span>100</span></div>
    <div class="scale-mark" style="top:146px"><span>75</span></div>
    <div class="scale-mark" style="top:275px"><span>50</span></div>
    <div class="scale-mark" style="top:405px"><span>25</span></div>
    <div class="scale-mark" style="top:536px"><span>0</span></div>
    <div class="tube">
      <div class="seg"></div><div class="seg"></div><div class="seg"></div><div class="seg"></div><div class="seg"></div>
      <div class="seg"></div><div class="seg"></div><div class="seg"></div><div class="seg"></div><div class="seg"></div>
      <div class="seg"></div><div class="seg"></div><div class="seg"></div><div class="seg"></div><div class="seg"></div>
      <div class="seg"></div><div class="seg"></div><div class="seg"></div><div class="seg"></div><div class="seg"></div>
    </div>
  </div>
</section>

<section class="generator generator--starboard">
  <div class="breaker" aria-label="Breaker closed">
    <svg width="92" height="152" viewBox="0 0 92 152">
      <defs><linearGradient id="poleOn" x1="0" x2="1"><stop offset="0" stop-color="#2a4a1a"/><stop offset=".5" stop-color="#7fb85a"/><stop offset="1" stop-color="#2e521e"/></linearGradient></defs>
      <rect x="42" y="21" width="7" height="112" fill="url(#poleOn)"/>
      <path d="M20 152 v-14 a10 10 0 0 1 10 -10 h32 a10 10 0 0 1 10 10 v14" fill="#000" stroke="#3c4680"/>
    </svg>
  </div>
  <header class="gen-header"><span class="gen-title">Starboard Generator</span><span class="gen-readout"><span>41<small>KW</small></span><span class="sep"></span><span>63%</span></span></header>
  <div class="controls">
    <div class="mode mode--online is-active">RUN ONLINE</div>
    <div class="mode mode--run is-ready">RUN</div>
    <div class="mode mode--stop is-ready">STOP</div>
    <div class="mode mode--auto is-off">AUTOMATIC</div>
  </div>
  <div class="status is-running"></div>
  <div class="info">
    <div class="info-divider"></div>
    <div class="field field--wide" style="top:34px"></div>
    <div class="field field--wide" style="top:98px"></div>
    <div class="field field--wide" style="top:162px"></div>
    <div class="field field--wide" style="top:226px"></div>
    <div class="field field--short" style="top:10px"></div>
    <div class="field field--short" style="top:40px"></div>
    <div class="field field--mid" style="top:69px"></div>
    <div class="field field--short" style="top:106px"></div>
    <div class="field field--short" style="top:136px"></div>
    <div class="field field--short" style="top:165px"></div>
    <div class="field field--short" style="top:205px"></div>
    <div class="field field--short" style="top:232px"></div>
  </div>
  <div class="load">
    <div class="scale-mark" style="top:16px"><span>100</span></div>
    <div class="scale-mark" style="top:146px"><span>75</span></div>
    <div class="scale-mark" style="top:275px"><span>50</span></div>
    <div class="scale-mark" style="top:405px"><span>25</span></div>
    <div class="scale-mark" style="top:536px"><span>0</span></div>
    <div class="tube">
      <div class="seg"></div><div class="seg"></div><div class="seg"></div><div class="seg"></div><div class="seg"></div>
      <div class="seg"></div><div class="seg"></div><div class="seg is-lit"></div><div class="seg is-lit"></div><div class="seg is-lit"></div>
      <div class="seg is-lit"></div><div class="seg is-lit"></div><div class="seg is-lit"></div><div class="seg is-lit"></div><div class="seg is-lit"></div>
      <div class="seg is-lit"></div><div class="seg is-lit"></div><div class="seg is-lit"></div><div class="seg is-lit"></div><div class="seg is-lit"></div>
    </div>
  </div>
</section>

</body>
</html>
```